Lanternleaf - Fresh Asian Cuisine Menu

We need to redo our menu to include pictures of food items. Our restaurant is vibrant, trendy, upscale Chinese cuisine

Requirements
Must have
• Must fit on 8.5x11 paper. We can remove the About Us section if needed but menu cannot be more than 6 pages total. Must include pictures of menu items

```html
<!DOCTYPE html>
<html lang="en">
<head>
<meta charset="utf-8">
<title>Lanternleaf - Lunch Menu</title>
<link href="https://fonts.googleapis.com/css2?family=Bebas+Neue&family=Oswald:wght@500;600&family=Roboto+Condensed:wght@400&family=Montserrat:wght@500;700&display=swap" rel="stylesheet">
<style>
  :root {
    --paper: #ffffff;
    --ink: #1c1c1c;
    --body: #3a3a3a;
    --accent: #e2412e;
    --photo-dark: #3b3a40;
    --photo-warm: #c9a27a;
  }
  * { margin: 0; padding: 0; box-sizing: border-box; }
  html, body { width: 927px; height: 1200px; overflow: hidden; background: var(--paper); }
  .menu { position: relative; width: 927px; height: 1200px; background: var(--paper); }

  .photo { position: absolute; left: 0; width: 269px; }
  .photo-1 { top: 0; height: 194px; background: radial-gradient(circle at 50% 45%, #b5532a 0%, #5b3a2a 40%, #2e3036 75%, #c8c0b8 100%); }
  .photo-2 { top: 210px; height: 182px; background: radial-gradient(circle at 55% 50%, #5a3b6a 0%, #3f6b3a 40%, #b9b2ad 70%, #e6a14a 100%); }
  .photo-3 { top: 409px; height: 190px; background: radial-gradient(circle at 50% 45%, #f08a2c 0%, #e7a24c 35%, #b7d27b 60%, #8a5a36 100%); }
  .photo-4 { top: 619px; height: 166px; background: radial-gradient(circle at 50% 50%, #3a2219 0%, #5e3a2a 30%, #f1eeea 55%, #6d6b70 100%); }
  .photo-5 { top: 802px; height: 182px; background: radial-gradient(circle at 45% 50%, #e8dcc0 0%, #6a3a22 35%, #2f7a2a 55%, #1e1e20 100%); }
  .photo-6 { top: 1001px; height: 199px; background: radial-gradient(circle at 50% 50%, #4a3128 0%, #9fc77c 30%, #ece9e3 55%, #5b4a44 100%); }

  .brand { position: absolute; top: 50px; left: 420px; width: 320px; text-align: center; }
  .brand-name { display: inline-flex; align-items: center; gap: 10px; font-family: "Montserrat", sans-serif; font-weight: 700; font-size: 40px; color: var(--ink); letter-spacing: 0.5px; line-height: 1; }
  .brand-dot { width: 16px; height: 16px; border-radius: 50%; background: var(--accent); }
  .brand-tag { margin-top: 6px; font-family: "Montserrat", sans-serif; font-weight: 700; font-size: 12px; color: var(--accent); letter-spacing: 1.4px; }

  .heading { position: absolute; top: 154px; left: 380px; width: 400px; text-align: center; }
  .heading h1 { font-family: "Oswald", sans-serif; font-weight: 600; font-size: 36px; color: var(--ink); line-height: 1; letter-spacing: 0.5px; }
  .heading p { font-family: "Montserrat", sans-serif; font-weight: 500; font-size: 13px; letter-spacing: 5px; color: var(--ink); line-height: 19px; }
  .heading p:first-of-type { margin-top: 8px; }

  .item { position: absolute; }
  .col-left .item { left: 325px; width: 257px; }
  .col-right .item { left: 607px; width: 255px; }
  .item h2 { font-family: "Bebas Neue", sans-serif; font-weight: 400; font-size: 17px; color: var(--accent); letter-spacing: 1.2px; line-height: 17px; width: 190px; }
  .item .price { position: absolute; top: -2px; right: 0; font-family: "Bebas Neue", sans-serif; font-size: 17px; color: var(--ink); }
  .item p { margin-top: 4px; font-family: "Roboto Condensed", sans-serif; font-size: 10px; line-height: 14px; color: var(--body); width: 215px; }
</style>
</head>
<body>
<main class="menu">
  <div class="photo photo-1" role="img" aria-label="Photo of Kung Pao chicken with peanuts on a dark plate"></div>
  <div class="photo photo-2" role="img" aria-label="Photo of stir fried eggplant and green beans in a white bowl"></div>
  <div class="photo photo-3" role="img" aria-label="Photo of orange chicken with lemon slices on lettuce"></div>
  <div class="photo photo-4" role="img" aria-label="Photo of glazed beef with broccoli on a white plate"></div>
  <div class="photo photo-5" role="img" aria-label="Photo of braised pork belly with rice cracker and broccoli"></div>
  <div class="photo photo-6" role="img" aria-label="Photo of shiitake mushrooms with baby bok choy"></div>

  <header class="brand">
    <div class="brand-name"><span class="brand-dot"></span>LANTERNLEAF</div>
    <div class="brand-tag">FRESH ASIAN CUISINE</div>
  </header>

  <section class="heading">
    <h1>LUNCH MENU</h1>
    <p>AVAILABLE MONDAY-FRIDAY</p>
    <p>FROM 11AM TO 3PM</p>
  </section>

  <section class="col-left">
    <div class="item" style="top:284px"><h2>Kung Pao Chicken</h2><span class="price">$10</span><p>Chicken sautéed with roasted peanuts and dry red chili in Kung Pao sauce</p></div>
    <div class="item" style="top:346px"><h2>Orange Chicken</h2><span class="price">$10</span><p>Battered-fried chicken breast with dried chili peppers and stir fried in a tangy orange flavored sauce</p></div>
    <div class="item" style="top:418px"><h2>Shredded Chicken in Spicy Garlic Sauce</h2><span class="price">$11</span><p>Tender shredded chicken, wood ear mushrooms, bamboo shoots, broccoli, green and red bell peppers and Chinese water chestnuts in a classic spicy garlic sauce</p></div>
    <div class="item" style="top:530px"><h2>Crispy Spicy Chicken</h2><span class="price">$11</span><p>Crispy-diced chicken with Sichuan peppers, garlic, scallions and red and green bell peppers</p></div>
    <div class="item" style="top:608px"><h2>General Tso's Chicken</h2><span class="price">$10</span><p>Battered-fried chicken breast, stir fried in a sweet &amp; tangy chili sauce with chili peppers</p></div>
    <div class="item" style="top:665px"><h2>Sweet &amp; Sour Chicken</h2><span class="price">$10</span><p>Crispy Chicken with green bell peppers, onions and pineapple glazed in a homemade sweet and sour marinade</p></div>
    <div class="item" style="top:740px"><h2>Oyster Beef</h2><span class="price">$11</span><p>Tender cuts of steak wok fried with onions and marinated in a homemade oyster sauce</p></div>
    <div class="item" style="top:802px"><h2>Black Pepper Steak</h2><span class="price">$12</span><p>Tender cuts of steak mixed with onions and red and green bell peppers</p></div>
    <div class="item" style="top:860px"><h2>Dancing Pork Belly</h2><span class="price">$11</span><p>Braised Pork Belly on sizzling rice cracker</p></div>
    <div class="item" style="top:905px"><h2>Twice Cooked Pork</h2><span class="price">$11</span><p>Stir fried Pork Belly slices with leek and fermented black beans</p></div>
    <div class="item" style="top:965px"><h2>Lemon Peel Shrimp</h2><span class="price">$12</span><p>Shrimp with fresh lemons in a sweet lemon sauce on a bed of shredded lettuce</p></div>
    <div class="item" style="top:1022px"><h2>Black Pepper Steak</h2><span class="price">$12</span><p>Tender cuts of steak mixed with onions and red and green bell peppers</p></div>
    <div class="item" style="top:1080px"><h2>Dancing Pork Belly</h2><span class="price">$11</span><p>Braised Pork Belly on sizzling rice cracker</p></div>
  </section>

  <section class="col-right">
    <div class="item" style="top:284px"><h2>Rice Wine Fish</h2><span class="price">$11</span><p>White fish filet with rice wine mixed with onions, peas and carrots</p></div>
    <div class="item" style="top:344px"><h2>Lanternleaf Fried Rice</h2><span class="price">$10</span><p>Shrimp, chicken, and beef, farm fresh eggs, onions, and scallions</p></div>
    <div class="item" style="top:418px"><h2>Vegetarian White Fried Rice</h2><span class="price">$9</span><p>Mixed vegetables with white rice</p></div>
    <div class="item" style="top:461px"><h2>Lanternleaf Lo Mein</h2><span class="price">$10</span><p>Shrimp, chicken, and beef, farm fresh eggs, onions, and scallions</p></div>
    <div class="item" style="top:521px"><h2>Vegetarian Lo Mein</h2><span class="price">$9</span><p>Mixed vegetables with lo mein noodles</p></div>
    <div class="item" style="top:568px"><h2>Mapo Tofu</h2><span class="price">$9</span><p>Soft Tofu, scallion, Sichuan peppercorn and peppers</p></div>
    <div class="item" style="top:628px"><h2>Spicy Garlic Eggplant</h2><span class="price">$10</span><p>Chinese eggplant in spicy garlic sauce garnished with scallions</p></div>
    <div class="item" style="top:689px"><h2>Stir Fried Eggplan</h2><span class="price">$10</span><p>Chinese eggplant with sautéed green beans</p></div>
    <div class="item" style="top:740px"><h2>Shiitake Baby Bok Choy</h2><span class="price">$10</span><p>Sautéed baby bok-choy with Shiitake mushrooms in brown sauce</p></div>
  </section>
</main>
</body>
</html>
```